Brisken. business card

We need a business card design for a new mobile car-wash catered toward urban residents. The use of colour should be black, white and red and should be sleek and minimal. The final design should be modern and enticing to look at. A picture of the logo is attached. The font and design should resemble something similar to the logo.

```html
<!DOCTYPE html>
<html lang="en">
<head>
<meta charset="utf-8">
<title>Brisken. business card</title>
<link rel="stylesheet" href="https://fonts.googleapis.com/css2?family=Michroma&display=swap">
<style>
  :root {
    --ink: #0b0b0b;
    --ink-soft: #1d1d1d;
    --red: #e8202a;
    --red-light: #f2454c;
    --white: #ffffff;
    --grey-text: #bdbdbd;
    --tile: #d8d8d8;
    --tile-icon: #3a3a3a;
    --backdrop: #cfcfcf;
  }
  * { margin: 0; padding: 0; box-sizing: border-box; }
  html, body { width: 1200px; height: 900px; overflow: hidden; }
  body {
    background: var(--backdrop);
    font-family: "Michroma", "Arial", sans-serif;
    color: var(--white);
    position: relative;
  }
  .card {
    position: absolute;
    left: 250px;
    width: 700px;
    height: 400px;
    background: radial-gradient(ellipse at 50% 35%, var(--ink-soft), var(--ink) 70%);
    overflow: hidden;
  }
  .card--front { top: 25px; }
  .card--back { top: 475px; }
  .card svg { position: absolute; left: 0; top: 0; }
  .card div { white-space: nowrap; }
  .wordmark {
    position: absolute;
    left: 0; right: 0;
    text-align: center;
    font-size: 46px;
    line-height: 1;
    letter-spacing: 4px;
    color: var(--white);
    text-transform: uppercase;
  }
  .card--front .wordmark { top: 132px; }
  .front-url {
    position: absolute;
    left: 0; right: 0; top: 262px;
    line-height: 22px;
    text-align: center;
    font-size: 18px;
    letter-spacing: 3px;
    color: var(--white);
  }
  .card--back .wordmark {
    top: 50px; left: 220px; right: 20px;
    font-size: 36px;
  }
  .person-name {
    position: absolute;
    top: 102px; left: 220px; right: 20px;
    text-align: center;
    font-size: 22px;
    line-height: 26px;
    letter-spacing: 10px;
  }
  .person-name .accent { color: var(--red); }
  .person-role {
    position: absolute;
    top: 138px; left: 220px; right: 20px;
    text-align: center;
    font-size: 11px;
    line-height: 14px;
    letter-spacing: 6px;
    color: var(--grey-text);
  }
  .contact {
    position: absolute;
    font-size: 14px;
    letter-spacing: 2px;
    color: var(--white);
    line-height: 28px;
  }
  .contact--phone { top: 200px; left: 0; width: 272px; text-align: right; }
  .contact--email { top: 236px; left: 0; width: 246px; text-align: right; }
  .contact--web { top: 264px; left: 452px; }
  .contact--address { top: 300px; left: 442px; }
</style>
</head>
<body>

<section class="card card--front" aria-label="Card front">
  <svg width="700" height="400" viewBox="0 0 700 400" aria-hidden="true">
    <rect x="0" y="246" width="700" height="8" fill="var(--red-light)"/>
    <rect x="0" y="256" width="700" height="34" fill="var(--red)"/>
  </svg>
  <div class="wordmark">Brisken.</div>
  <div class="front-url">WWW.BRISKEN.COM</div>
</section>

<section class="card card--back" aria-label="Card back">
  <svg width="700" height="400" viewBox="0 0 700 400" aria-hidden="true">
    <polygon points="0,200 290,200 280,228 0,228" fill="var(--red)"/>
    <polygon points="0,236 266,236 256,264 0,264" fill="var(--red)"/>
    <polygon points="300,200 360,200 350,228 290,228" fill="var(--tile)"/>
    <polygon points="368,200 440,200 430,228 358,228" fill="var(--tile)"/>
    <polygon points="276,236 338,236 328,264 266,264" fill="var(--tile)"/>
    <polygon points="346,236 420,236 410,264 336,264" fill="var(--tile)"/>
    <rect x="321" y="205" width="10" height="18" rx="2" fill="var(--tile-icon)"/>
    <rect x="323" y="208" width="6" height="8" fill="var(--tile)"/>
    <circle cx="399" cy="214" r="8" fill="none" stroke="var(--tile-icon)" stroke-width="1.6"/>
    <ellipse cx="399" cy="214" rx="3.5" ry="8" fill="none" stroke="var(--tile-icon)" stroke-width="1.4"/>
    <line x1="391" y1="214" x2="407" y2="214" stroke="var(--tile-icon)" stroke-width="1.4"/>
    <rect x="291" y="243" width="20" height="14" fill="var(--tile-icon)"/>
    <polyline points="291,243 301,251 311,243" fill="none" stroke="var(--tile)" stroke-width="1.5"/>
    <polygon points="378,240 368,249 388,249" fill="var(--tile-icon)"/>
    <rect x="371" y="249" width="14" height="10" fill="var(--tile-icon)"/>
    <polygon points="440,264 700,264 700,292 430,292" fill="var(--red)"/>
    <polygon points="430,300 700,300 700,328 420,328" fill="var(--red)"/>
  </svg>
  <div class="wordmark">Brisken.</div>
  <div class="person-name"><span class="accent">A</span>LEX MARLO<span class="accent">W</span></div>
  <div class="person-role">PROJECT DIRECTOR</div>
  <div class="contact contact--phone">041 555 0142</div>
  <div class="contact contact--email">hello@brisken.com</div>
  <div class="contact contact--web">www.brisken.com</div>
  <div class="contact contact--address">harbor lane 214, NY</div>
</section>

</body>
</html>
```